Letterhead & Business Card Design Project

Use existing logo to create a new letterhead and business card design. Looking for something clean modern using color options of black, white and gray. The green from the logo may be used lightly as an accent color.

Target Market(s)

Professional business people

Industry/Entity Type

Business

Requirements
Must have
• Business card with front and back design using existing logo.
Nice to have
• Professional presentation
Clean look
Should not have
• No oil rigs, pumpjacks or clip art.

```html
<!DOCTYPE html>
<html lang="en">
<head>
<meta charset="utf-8">
<title>Halvern Resources – Business Card</title>
<link rel="stylesheet" href="https://fonts.googleapis.com/css2?family=Marcellus&family=Lato:wght@300;400&display=swap">
<style>
  :root {
    --backdrop: #d9d9d9;
    --card-back: #9c9c9c;
    --card-front: #f7f7f5;
    --ink-dark: #2a2a2a;
    --ink-mid: #7a7a7a;
    --ink-light: #ffffff;
    --accent-green: #4caf3f;
  }
  * { margin: 0; padding: 0; box-sizing: border-box; }
  html, body {
    width: 1200px; height: 900px; overflow: hidden;
    background: var(--backdrop);
  }
  .canvas { position: relative; width: 1200px; height: 900px; }
  .card {
    position: absolute; left: 250px; width: 700px; height: 400px;
    box-shadow: 0 6px 18px rgba(0,0,0,0.18);
  }
  .card--back { top: 40px; background: var(--card-back); }
  .card--front { top: 470px; background: var(--card-front); }

  .wordmark {
    font-family: "Marcellus", serif;
    color: var(--ink-dark);
    text-transform: uppercase;
    white-space: nowrap;
  }
  .card--back .wordmark {
    position: absolute; left: 0; right: 0; top: 150px;
    text-align: center; font-size: 42px; letter-spacing: 6px;
  }
  .web-address {
    position: absolute; left: 0; right: 0; top: 262px;
    text-align: center;
    font-family: "Lato", sans-serif; font-weight: 400;
    font-size: 19px; letter-spacing: 1px; color: var(--ink-light);
  }

  .card--front .wordmark {
    position: absolute; left: 48px; top: 44px;
    font-size: 28px; letter-spacing: 4px;
  }
  .holder {
    position: absolute; left: 48px; top: 150px;
    font-family: "Lato", sans-serif; color: var(--ink-mid);
  }
  .holder__name { font-weight: 300; font-size: 30px; }
  .holder__role { font-weight: 400; font-size: 18px; text-transform: uppercase; }
  .contact-list {
    position: absolute; left: 48px; top: 250px; list-style: none;
    font-family: "Lato", sans-serif; font-weight: 300;
    font-size: 17px; line-height: 25px; color: var(--ink-mid);
  }
  .contact-list__label {
    display: inline-block; width: 20px;
    color: var(--accent-green); font-weight: 400;
  }
  .postal-address {
    position: absolute; left: 440px; top: 280px; font-style: normal;
    font-family: "Lato", sans-serif; font-weight: 300;
    font-size: 17px; line-height: 24px; color: var(--ink-mid);
  }
</style>
</head>
<body>
<main class="canvas">
  <section class="card card--back" aria-label="Business card back">
    <div class="wordmark">Halvern Resources</div>
    <div class="web-address">www.halvernresources.com</div>
  </section>

  <section class="card card--front" aria-label="Business card front">
    <div class="wordmark">Halvern Resources</div>
    <div class="holder">
      <span class="holder__name">Tobias Renfeld</span>
      <span class="holder__role">| Manager</span>
    </div>
    <ul class="contact-list">
      <li><span class="contact-list__label">t</span>555.214.3380</li>
      <li><span class="contact-list__label">f</span>555.214.3381</li>
      <li><span class="contact-list__label">e</span>tobias@halvernresources.com</li>
    </ul>
    <address class="postal-address">
      4120 North Birch Ave<br>
      Suite 240<br>
      Dunmore, Kansas 66012
    </address>
  </section>
</main>
</body>
</html>
```